St. Paddy’s Day Invitation

Invitation to text to people:
6th Annual St. Paddy’s Day Party
Where: The Kelterbrook’s
When: Saturday, March 25
Acoustic session by Taddeo Lindqvist from Mr. Pocketwatch
Fundraiser for Milo Ferreday ‘Open Harbor’ Fund

Target Market(s)

Adults only, all friends from our town, Moorestown, NJ

Colors
00AB8E
00BBA5
67D7C9
C6EFE9
E9F9F6
59FF00
82FF00
B8FF75
E3FFCB
F4FFEA

```html
<!DOCTYPE html>
<html lang="en">
<head>
<meta charset="utf-8">
<title>6th Annual St. Paddy’s Day Party</title>
<link rel="stylesheet" href="https://fonts.googleapis.com/css2?family=Uncial+Antiqua&family=Poppins:wght@300;400;700&display=swap">
<style>
  :root {
    --green-deep: #0b5a22;
    --green-mid: #167a2c;
    --green-light: #2a9a3a;
    --yellow: #eef218;
    --white: #ffffff;
    --photo-warm: #8c7f70;
    --photo-dark: #2d2a27;
    --photo-sky: #c9d4de;
    --photo-wall: #e7e2dc;
    --photo-shadow: #4f555b;
  }
  * { margin: 0; padding: 0; box-sizing: border-box; }
  html, body { width: 857px; height: 1200px; overflow: hidden; }
  body { background: var(--green-deep); }
  .invitation {
    position: relative;
    width: 857px;
    height: 1200px;
    overflow: hidden;
    font-family: "Poppins", sans-serif;
    color: var(--white);
    background:
      radial-gradient(ellipse at 50% 35%, var(--green-light) 0%, var(--green-mid) 45%, var(--green-deep) 100%);
  }

  .title { position: absolute; inset: 0; color: var(--yellow); font-family: "Uncial Antiqua", serif; }
  .title__number {
    position: absolute; left: 150px; top: 72px;
    font-size: 232px; line-height: 1;
  }
  .title__ordinal {
    position: absolute; left: 312px; top: 92px;
    font-size: 34px; line-height: 1;
  }
  .title__line { position: absolute; font-size: 54px; line-height: 1; white-space: nowrap; }
  .title__line--annual { left: 398px; top: 80px; }
  .title__line--saint { left: 332px; top: 164px; }
  .title__line--party { left: 358px; top: 248px; }

  .details { position: absolute; top: 388px; width: 857px; height: 200px; }
  .details__col { position: absolute; top: 0; width: 320px; text-align: center; }
  .details__col--where { left: 54px; }
  .details__col--when { left: 469px; }
  .details__label { font-size: 27px; font-weight: 300; letter-spacing: 1px; line-height: 1.2; }
  .details__value { font-size: 38px; font-weight: 700; color: var(--yellow); line-height: 1.62; margin-top: 4px; }
  .details__divider { position: absolute; left: 427px; top: 4px; width: 2px; height: 186px; background: var(--yellow); }

  .photo {
    position: absolute; border-radius: 50%;
    border: 3px solid var(--yellow);
  }
  .photo--band {
    left: 88px; top: 600px; width: 308px; height: 308px;
    background: radial-gradient(circle at 50% 55%, var(--photo-warm) 0%, var(--photo-dark) 80%);
  }
  .photo--child {
    left: 525px; top: 863px; width: 246px; height: 246px;
    background: linear-gradient(180deg, var(--photo-wall) 0%, var(--photo-sky) 45%, var(--photo-shadow) 78%);
  }

  .performer { position: absolute; left: 436px; top: 650px; line-height: 1.25; }
  .performer__intro { font-size: 30px; font-weight: 400; }
  .performer__name { font-size: 37px; font-weight: 700; color: var(--yellow); }
  .performer__band { font-size: 27px; font-weight: 400; }

  .fundraiser { position: absolute; left: 88px; top: 995px; }
  .fundraiser__intro { font-size: 29px; font-weight: 400; line-height: 1.3; }
  .fundraiser__name { font-size: 40px; font-weight: 700; color: var(--yellow); line-height: 1.3; }

  .fund-mark {
    position: absolute; left: 548px; top: 1050px; width: 200px;
    text-align: center; font-size: 18px; font-weight: 700; color: var(--white);
    line-height: 1.2; text-transform: uppercase; white-space: nowrap;
  }
</style>
</head>
<body>
  <main class="invitation">
    <header class="title">
      <div class="title__number">6</div>
      <div class="title__ordinal">th</div>
      <div class="title__line title__line--annual">Annual</div>
      <div class="title__line title__line--saint">St. Paddy’s</div>
      <div class="title__line title__line--party">Day Party</div>
    </header>

    <section class="details">
      <div class="details__col details__col--where">
        <p class="details__label">where</p>
        <p class="details__value">The<br>Kelterbrook’s</p>
      </div>
      <div class="details__divider"></div>
      <div class="details__col details__col--when">
        <p class="details__label">when</p>
        <p class="details__value">Saturday,<br>March 25</p>
      </div>
    </section>

    <div class="photo photo--band" role="img" aria-label="Black and white photo of the band Mr. Pocketwatch"></div>

    <section class="performer">
      <p class="performer__intro">Acoustic session by</p>
      <p class="performer__name">Taddeo Lindqvist</p>
      <p class="performer__band">from Mr. Pocketwatch</p>
    </section>

    <section class="fundraiser">
      <p class="fundraiser__intro">Fundraiser for</p>
      <p class="fundraiser__name">Milo Ferreday<br>‘Open Harbor’ Fund</p>
    </section>

    <div class="photo photo--child" role="img" aria-label="Photo of Milo Ferreday, a smiling boy in a baseball cap"></div>
    <div class="fund-mark">Open Harbor Fund</div>
  </main>
</body>
</html>
```